Tax Business Advertisement

Whitfield & Associates Tax Services - Need to develop an advertisement tool suitable for print and electronic advertising. My business provides tax preparation and audit representation for Individuals, Partnerships, Corporations, Estates, Trusts and other entities with tax reporting requirements. I recently had business cards designed by your company, design #4827305 and would need the basic information from the business card on the advertisement.

Some of the following wording may be suitable for the advertisement:

Enrolled Agents are licensed to practice by the NRB. Our services include personal and business tax return preparation, tax audits, offers in compromise, back taxes, forming new business, dissolving business, and much more. We are available to provide services in all 50 states.

Enrolled agents are the only federally licensed tax practitioners who specialize in taxation and who have unlimited rights to represent taxpayers before the NRB.

If you are just starting a business, have been in business for a long time, or just an individual who needs a Tax Professional, Whitfield & Associates Tax Services is the right choice for you.

```html
<!DOCTYPE html>
<html lang="en">
<head>
<meta charset="utf-8">
<title>Whitfield &amp; Associates Tax Services</title>
<link rel="stylesheet" href="https://fonts.googleapis.com/css2?family=Crimson+Text:wght@400;600;700&display=swap">
<style>
:root{
  --red:#c8282d;
  --red-dark:#7a1216;
  --ink:#1f1f1f;
  --black:#111;
  --cream:#fbe9d6;
  --paper:#fff;
  --photo-light:#e6e9ee;
  --photo-mid:#b9c4d2;
}
*{margin:0;padding:0;box-sizing:border-box}
html,body{width:927px;height:1200px;overflow:hidden;background:var(--paper)}
.ad{position:relative;width:927px;height:1200px;font-family:"Crimson Text",serif;color:var(--ink)}
.hero{position:absolute;left:0;top:0;width:927px;height:556px;
  background:linear-gradient(160deg,var(--photo-light) 0%,#f4f4f2 40%,var(--photo-mid) 75%,#9fae9a 100%)}
.hero-swoosh{position:absolute;left:0;top:0}
.hero-band{position:absolute;left:0;top:555px;width:927px;height:24px;
  background:linear-gradient(90deg,var(--red-dark) 0%,var(--red) 30%,#d94a47 50%,var(--red) 70%,var(--red-dark) 100%)}
.copy{position:absolute;left:43px;font-size:23.5px;line-height:22.7px}
.intro{top:603px;width:860px}
.points{top:726px;width:380px}
.points p+p{margin-top:22.7px}
.brand{position:absolute;left:440px;top:752px;display:flex;align-items:center;gap:16px}
.brand-mark{width:22px;height:22px;background:var(--red)}
.brand-name{font-size:34px;font-weight:600;color:#222;letter-spacing:.3px}
.contact{position:absolute;left:432px;top:852px;width:448px;height:186px;background:var(--red);
  box-shadow:4px 4px 0 #2a2a2a}
.contact-photo{position:absolute;left:23px;top:14px;width:115px;height:158px;
  background:linear-gradient(180deg,#e9e6e0 0%,#bfb7ad 55%,#2b2b2e 100%)}
.contact-info{position:absolute;left:159px;top:16px;color:var(--cream);font-size:20px;line-height:25px}
.contact-info h2{font-size:20px;font-weight:700;color:#fff;line-height:25px}
.footer{position:absolute;left:0;top:1075px}
.site{position:absolute;left:0;top:1120px;width:927px;text-align:center;color:#fff;
  font-size:31px;font-weight:700;letter-spacing:.3px}
</style>
</head>
<body>
<div class="ad">
  <div class="hero" role="img" aria-label="Photo of a tax return form with a benefits card, reading glasses and a banknote"></div>
  <svg class="hero-swoosh" width="927" height="110" viewBox="0 0 927 110" aria-hidden="true">
    <defs>
      <linearGradient id="swoosh" x1="0" x2="1" y1="0" y2="0">
        <stop offset="0" stop-color="#111"/><stop offset="0.6" stop-color="#3a0c0e"/><stop offset="1" stop-color="#c8282d"/>
      </linearGradient>
    </defs>
    <path d="M0 0H560C430 40 230 75 0 100Z" fill="url(#swoosh)"/>
    <path d="M0 100C230 75 430 40 560 0H590C450 48 240 86 0 108Z" fill="#c8282d"/>
  </svg>
  <div class="hero-band"></div>

  <p class="copy intro">Enrolled Agents are licensed to practice by the NRB. Our services include personal and business tax return preparation, tax audits, offers in compromise, back taxes, forming new business, dissolving business, and much more. We are available to provide services in all 50 states.</p>

  <div class="copy points">
    <p>Enrolled agents are the only federally licensed tax practitioners who specialize in taxation and who have unlimited rights to represent taxpayers before the NRB.</p>
    <p>If you are just starting a business, have been in business for a long time, or just an individual who needs a Tax Professional, Whitfield &amp; Associates Tax Services is the right choice for you.</p>
  </div>

  <div class="brand">
    <span class="brand-mark"></span>
    <span class="brand-name">Whitfield &amp; Associates</span>
  </div>

  <div class="contact">
    <div class="contact-photo" role="img" aria-label="Portrait of the enrolled agent"></div>
    <div class="contact-info">
      <h2>CONTACT US NOW!</h2>
      <p>Daniel R. Whitfield II, EA, MS</p>
      <p>P05817369 | (555) 318-4620</p>
      <p>taxdesk411@example.com</p>
      <p>4120 Meadow Lane, Suite D,</p>
      <p>Fairhaven, CA 95000</p>
    </div>
  </div>

  <svg class="footer" width="927" height="125" viewBox="0 0 927 125" aria-hidden="true">
    <defs>
      <linearGradient id="foot" x1="0" x2="1">
        <stop offset="0" stop-color="#111"/><stop offset="0.5" stop-color="#c8282d"/><stop offset="1" stop-color="#111"/>
      </linearGradient>
    </defs>
    <path d="M0 20C300 0 630 0 927 20V125H0Z" fill="url(#foot)"/>
    <path d="M0 34C300 18 630 18 927 34V125H0Z" fill="#151515"/>
  </svg>
  <p class="site">www.taxhelpforevery.com</p>
</div>
</body>
</html>
```